Create a flyer for our party getaway to Ibiza.

'The Velvet Ibiza Getaway'

Friday 14th July - Monday 17th July

DJ Korvex & DJ Tamblin brings together a jam-packed weekend schedule full of the best urban parties in Ibiza.

What's included?

4 Nights Of Entertainment
6 Parties In Total
1 Boat Party
1 Pool Party
2 Superclub Parties
1 Indoor Water Party
Bottomless Drinks (Boat Party Only)
An unbelievable experience
1 unbeatable price.

All this for 140€ (you save 50€ when you book with us)

Tickets avaialble from Ticketmoor & Queldrix

Target Market(s)

holiday goers

Industry/Entity Type

party, events, club, hip hop

Requirements
Must have
• good vibes
Nice to have
• nice catchy looking title

```html
<!DOCTYPE html>
<html lang="en">
<head>
<meta charset="utf-8">
<title>The Velvet Ibiza Getaway</title>
<link rel="stylesheet" href="https://fonts.googleapis.com/css2?family=Montserrat:wght@300;600;700;800;900&family=Barlow:wght@500&family=Yellowtail&display=swap">
<style>
  :root {
    --page-top: #12062a;
    --page-bottom: #3c1163;
    --ink: #ffffff;
    --gold: #ffc21a;
    --gold-deep: #ff9a0a;
    --magenta: #e21cf2;
    --violet: #a72ad6;
    --panel: rgba(14, 6, 34, 0.78);
    --ticket: #f97a1e;
  }
  * { margin: 0; padding: 0; box-sizing: border-box; }
  html, body { width: 848px; height: 1200px; overflow: hidden; }
  body {
    background: linear-gradient(180deg, var(--page-top) 0%, #24093f 60%, var(--page-bottom) 100%);
    font-family: "Montserrat", sans-serif;
    color: var(--ink);
    position: relative;
  }
  .flyer {
    position: absolute; left: 39px; top: 55px; width: 770px; height: 1089px;
    overflow: hidden;
    background: linear-gradient(180deg, #3b1266 0%, #4a1a7a 30%, #2e1470 62%, #1d1466 82%, #2a0f5c 100%);
  }
  .club-scene {
    position: absolute; inset: 0;
    background:
      radial-gradient(ellipse 260px 180px at 330px 120px, rgba(230, 60, 110, 0.55), transparent 70%),
      radial-gradient(ellipse 220px 160px at 560px 160px, rgba(120, 70, 200, 0.45), transparent 70%),
      radial-gradient(ellipse 500px 240px at 385px 1000px, rgba(20, 10, 60, 0.7), transparent 70%);
  }
  .dj-photo {
    position: absolute; left: 91px; top: 50px; width: 513px; height: 370px;
    border-radius: 40px 40px 0 0;
    background:
      radial-gradient(ellipse 140px 190px at 155px 200px, rgba(235, 220, 245, 0.55), transparent 75%),
      radial-gradient(ellipse 150px 190px at 360px 220px, rgba(235, 225, 240, 0.5), transparent 75%),
      linear-gradient(180deg, rgba(200, 70, 120, 0.25), rgba(80, 30, 120, 0));
  }
  .brand {
    position: absolute; left: 33px; top: 36px;
    font-weight: 800; font-size: 38px; letter-spacing: -1px; color: var(--ink);
  }
  .title { position: absolute; left: 0; width: 770px; text-align: center; }
  .title-top {
    top: 352px; font-weight: 800; font-size: 52px; letter-spacing: -1.5px; line-height: 1;
  }
  .title-main {
    top: 405px; font-weight: 900; font-size: 78px; letter-spacing: 4px; line-height: 1;
    background: linear-gradient(180deg, var(--gold) 30%, var(--gold-deep) 100%);
    -webkit-background-clip: text; background-clip: text; color: transparent;
  }
  .rule { position: absolute; left: 110px; top: 499px; width: 550px; height: 1px; background: var(--gold); }
  .dates {
    position: absolute; left: 0; top: 508px; width: 770px; text-align: center;
    font-family: "Barlow", sans-serif; font-weight: 500; font-size: 38px; line-height: 1.2;
  }
  .dates sup { font-size: 19px; vertical-align: 15px; line-height: 0; }
  .included {
    position: absolute; left: 46px; top: 574px; width: 394px; height: 416px;
    background: var(--panel); border-radius: 20px;
  }
  .included-heading {
    position: absolute; left: 22px; top: 6px;
    font-family: "Yellowtail", cursive; font-size: 58px; color: var(--gold); line-height: 1.2;
  }
  .perk { position: absolute; display: flex; align-items: center; gap: 8px; }
  .perk-count { font-weight: 800; font-size: 46px; color: var(--gold); line-height: 1; width: 30px; text-align: center; }
  .perk-label { font-weight: 700; font-size: 16.5px; line-height: 1.15; }
  .extra { position: absolute; font-weight: 700; font-size: 16.5px; line-height: 1.15; }
  .closing { position: absolute; left: 0; width: 394px; top: 380px; text-align: center; font-weight: 700; font-size: 16px; }
  .price-box {
    position: absolute; left: 461px; top: 595px; width: 262px; height: 162px;
    background: var(--panel); border-radius: 18px; text-align: center;
  }
  .price-lead { margin-top: 22px; font-weight: 700; font-size: 30px; line-height: 1; }
  .price-figure {
    margin-top: 6px; font-weight: 900; font-size: 84px; line-height: 1; letter-spacing: -2px;
    background: linear-gradient(90deg, var(--violet), var(--magenta));
    -webkit-background-clip: text; background-clip: text; color: transparent;
  }
  .saving {
    position: absolute; left: 461px; top: 780px; width: 262px; text-align: center;
    font-weight: 700; font-size: 20px; line-height: 1.3;
  }
  .saving em { font-style: normal; color: var(--gold); }
  .ticket-seller {
    position: absolute; left: 482px; top: 882px; width: 222px; text-align: center;
    font-weight: 700; font-size: 36px; color: var(--ticket);
  }
  .tickets {
    position: absolute; left: 0; top: 1025px; width: 770px; text-align: center;
    font-weight: 300; font-size: 24px;
  }
  .tickets strong { font-weight: 700; }
</style>
</head>
<body>
  <main class="flyer">
    <div class="club-scene" role="img" aria-label="Night club crowd with stage lights and hands in the air"></div>
    <div class="dj-photo" role="img" aria-label="Photo of the two DJs in white t-shirts posing at the decks"></div>

    <div class="brand">Queldrix</div>

    <h1>
      <span class="title title-top">THE VELVET IBIZA</span>
      <span class="title title-main">GETAWAY</span>
    </h1>
    <div class="rule"></div>
    <p class="dates">Friday 14<sup>th</sup> July - Monday 17<sup>th</sup> July</p>

    <section class="included">
      <h2 class="included-heading">Whats included?</h2>
      <div class="perk" style="left:28px;top:148px"><span class="perk-count">4</span><span class="perk-label">Nights Of<br>Entertainment</span></div>
      <div class="perk" style="left:225px;top:148px"><span class="perk-count">1</span><span class="perk-label">Pool<br>Party</span></div>
      <div class="perk" style="left:28px;top:212px"><span class="perk-count">6</span><span class="perk-label">Parties in<br>Total</span></div>
      <div class="perk" style="left:225px;top:212px"><span class="perk-count">2</span><span class="perk-label">Superclub<br>Parties</span></div>
      <div class="perk" style="left:28px;top:277px"><span class="perk-count">1</span><span class="perk-label">Boat<br>Party</span></div>
      <div class="perk" style="left:225px;top:277px"><span class="perk-count">2</span><span class="perk-label">Indoor<br>Water Party</span></div>
      <p class="extra" style="left:33px;top:343px">Bottomless Drinks<br>(Boat Party Only)</p>
      <p class="extra" style="left:231px;top:343px">An unbelievable<br>experience</p>
      <p class="closing">1 unbeatable price.</p>
    </section>

    <section class="price-box">
      <p class="price-lead">ALL THIS FOR</p>
      <p class="price-figure">140€</p>
    </section>
    <p class="saving">YOU SAVE <em>50€</em> WHEN<br>YOU BOOK WITH US</p>
    <p class="ticket-seller">Ticketmoor</p>

    <p class="tickets">Tickets avaialble from <strong>Ticketmoor</strong> &amp; <strong>Queldrix</strong></p>
  </main>
</body>
</html>
```